Need to make a work slip for trucking company.

I need a form to fill out for my truck drivers to get signed on delivery. It is for a trucking company and this form will be for each machine equipment move. I have included my old sheet which I need Updated. Its going on a 9.5 inch by 8.5 inch sheet of paper. It should have room for the day, date, customer name, ordered by, P.O. Number, Project Number, Driver, Truck/Trailer, Tolls (needs more room then my old sheet need a few lines under each other for each toll during the machine move), Permits, some room for other information, Loads, Hours, and 2 lines for a Signature and Print Line.
Updates

Need to also include a Pickup Address and a Deliver Address with lines to write in. Also I need to add a Print Line (and labeled Print) for whoever is signing the ticket.

Requirements
Must have
• My new company name and Logo. I have included my new Logo. It must be easy to ready. Must include my company colors. (Concrete Gray, and Neon Blue)

```html
<!DOCTYPE html>
<html lang="en">
<head>
<meta charset="utf-8">
<title>Kestrel Haulage – Work Slip</title>
<link href="https://fonts.googleapis.com/css2?family=Figtree:wght@400;500;700;800&display=swap" rel="stylesheet">
<style>
  :root{
    --neon-blue:#126fbc;
    --concrete:#ececec;
    --ink:#222428;
    --rule:#8c8c8c;
    --ticket-red:#ee1c1c;
    --page:#ffffff;
    --backdrop:#e4e4e6;
  }
  *{margin:0;padding:0;box-sizing:border-box}
  html,body{width:1200px;height:1069px;overflow:hidden;background:var(--backdrop)}
  body{font-family:'Figtree',sans-serif;color:var(--ink)}
  .work-slip{
    position:absolute;left:5px;top:3px;width:1870px;height:1672px;
    transform:scale(0.636);transform-origin:0 0;background:var(--page);
  }
  .frame{position:absolute;inset:0;width:1870px;height:1672px}
  .sheet{position:absolute;left:31px;top:27px;width:1801px;height:1615px;background:var(--page);border:2px solid #f0f0f0}
  .letterhead{position:absolute;left:0;top:0;width:100%;height:243px;background:var(--concrete)}
  .ticket-no{position:absolute;left:39px;top:26px;font-size:38px;font-weight:700;color:var(--ticket-red)}
  .brand{position:absolute;left:0;width:100%;top:42px;text-align:center;font-size:66px;font-weight:800;color:var(--neon-blue);letter-spacing:1px}
  .contact{position:absolute;left:0;width:100%;top:170px;display:flex;justify-content:center;align-items:center;gap:26px;font-size:32px;font-weight:500}
  .contact .item{display:flex;align-items:center;gap:14px}
  .contact svg{width:46px;height:46px}
  .label{position:absolute;font-size:31px;font-weight:500;white-space:nowrap;line-height:1}
  .label.right{text-align:right}
  .rule{position:absolute;height:2px;background:var(--rule)}
  .days{position:absolute;left:37px;top:277px;font-size:28px;font-weight:500;word-spacing:14px;letter-spacing:1px}
  .ampm{position:absolute;left:85px;top:322px;font-size:28px;font-weight:500}
  .equipment{position:absolute;left:0;width:100%;top:610px;text-align:center;font-size:29px;font-weight:500;word-spacing:4px}
</style>
</head>
<body>
<div class="work-slip">
  <svg class="frame" viewBox="0 0 1870 1672" aria-hidden="true">
    <polygon fill="#126fbc" points="0,0 916,0 890,27 31,27 31,888 0,918"/>
    <polygon fill="#126fbc" points="1870,755 1870,1672 953,1672 983,1642 1832,1642 1832,793"/>
  </svg>
  <div class="sheet">
    <header class="letterhead">
      <div class="ticket-no">19234</div>
      <div class="brand">KESTREL HAULAGE</div>
      <div class="contact">
        <span class="item">
          <svg viewBox="0 0 46 46"><circle cx="23" cy="23" r="21" fill="none" stroke="#126fbc" stroke-width="2.5"/><path d="M23 10c-5.5 0-9 4-9 8.5 0 6 9 16.5 9 16.5s9-10.5 9-16.5C32 14 28.5 10 23 10z" fill="#126fbc"/><circle cx="23" cy="18.5" r="3.5" fill="#fff"/></svg>
          Harbor Point, New York 10999
        </span>
        <span>|</span>
        <span class="item">
          <svg viewBox="0 0 46 46"><circle cx="23" cy="23" r="21" fill="none" stroke="#126fbc" stroke-width="2.5"/><path d="M15 12c2-1 3-1 4 1l2 4c.5 1.5 0 2.5-1.5 3.5 1 3 3 5 6 6.5 1-1.5 2-2 3.5-1.5l4 2c2 1 2 2 1 4-1.5 2.5-4 3-7 1.5-6-3-10-7.5-12.5-13-1.5-3-1-6.5.5-8z" fill="#126fbc"/></svg>
          ( 555 ) 014-3000
        </span>
        <span>|</span>
        <span class="item">
          <svg viewBox="0 0 46 46"><circle cx="23" cy="23" r="21" fill="none" stroke="#126fbc" stroke-width="2.5"/><rect x="16" y="13" width="14" height="8" fill="#126fbc"/><rect x="12" y="19" width="22" height="14" rx="2" fill="#126fbc"/><rect x="19" y="23" width="11" height="2" fill="#fff"/><rect x="19" y="27" width="11" height="2" fill="#fff"/></svg>
          ( 555 ) 014-3009
        </span>
      </div>
    </header>

    <div class="days">M T W T F S S</div>
    <div class="ampm">A.M. / P.M</div>

    <div class="label" style="left:1293px;top:296px">Date :</div>
    <div class="rule" style="left:1379px;top:325px;width:385px"></div>

    <div class="label" style="left:38px;top:415px">Customer Name :</div>
    <div class="rule" style="left:296px;top:445px;width:560px"></div>
    <div class="label right" style="left:969px;top:415px">Ordered By :</div>
    <div class="rule" style="left:1165px;top:445px;width:600px"></div>

    <div class="label" style="left:38px;top:490px">P.O. Number :</div>
    <div class="rule" style="left:296px;top:521px;width:560px"></div>
    <div class="label right" style="left:908px;top:490px">Project Number :</div>
    <div class="rule" style="left:1165px;top:521px;width:600px"></div>

    <div class="equipment">F/B &nbsp;*&nbsp; L / B &nbsp;*&nbsp; STR / TRL &nbsp;*&nbsp; BM / TK &nbsp;*&nbsp; DUMP TK &nbsp;*&nbsp; ROLL BACK &nbsp;*&nbsp; ROLL OFF</div>

    <div class="label" style="left:38px;top:686px">Driver :</div>
    <div class="rule" style="left:262px;top:716px;width:594px"></div>
    <div class="label" style="left:38px;top:765px">Truck/Trailer :</div>
    <div class="rule" style="left:262px;top:795px;width:594px"></div>

    <div class="label" style="left:38px;top:842px">Tolls :</div>
    <div class="rule" style="left:262px;top:872px;width:594px"></div>
    <div class="rule" style="left:262px;top:932px;width:594px"></div>
    <div class="rule" style="left:262px;top:992px;width:594px"></div>
    <div class="rule" style="left:262px;top:1053px;width:594px"></div>

    <div class="label" style="left:38px;top:1099px">Permits :</div>
    <div class="rule" style="left:262px;top:1130px;width:594px"></div>
    <div class="rule" style="left:262px;top:1190px;width:594px"></div>

    <div class="label" style="left:38px;top:1234px">Others :</div>
    <div class="rule" style="left:262px;top:1265px;width:594px"></div>
    <div class="rule" style="left:262px;top:1325px;width:594px"></div>

    <div class="label" style="left:38px;top:1431px">Loads :</div>
    <div class="rule" style="left:262px;top:1462px;width:315px"></div>
    <div class="label" style="left:38px;top:1507px">Hours :</div>
    <div class="rule" style="left:262px;top:1537px;width:315px"></div>

    <div class="label right" style="left:992px;top:1431px">Signature :</div>
    <div class="rule" style="left:1167px;top:1462px;width:598px"></div>
    <div class="label right" style="left:992px;top:1507px">Print Line :</div>
    <div class="rule" style="left:1167px;top:1537px;width:598px"></div>
  </div>
</div>
</body>
</html>
```